Harbourlight ceramics Ltd
Stone and tile specialists
Simple
Colin Ashby-Rhodes
Director
Address not needed on the business card
colin@harbourlightceramics.example
www.harbourlightceramics.example
We also require an A4 folder promotional sheet, a letter head, complimentry slip and a van design.
Logo and the web address. All other info on the other side. In UK we say mob: instead of cell.

```html
<!DOCTYPE html>
<html lang="en">
<head>
<meta charset="utf-8">
<title>Harbourlight ceramics Ltd — Business Card</title>
<link rel="stylesheet" href="https://fonts.googleapis.com/css2?family=Questrial&family=Arimo:wght@700&family=Tinos&display=swap">
<style>
  :root {
    --stage: #2b2b2b;
    --card: #ffffff;
    --accent: #f26a1b;
    --ink-grey: #7a7a7a;
    --text-dark: #333333;
    --divider: #d4d4d4;
  }
  * { margin: 0; padding: 0; box-sizing: border-box; }
  html, body { width: 1200px; height: 780px; overflow: hidden; }
  body { background: var(--stage); position: relative; }

  .business-card {
    position: absolute;
    left: 150px; top: 120px;
    width: 900px; height: 540px;
    background: var(--card);
    border-radius: 34px;
    overflow: hidden;
  }
  .edge-tab {
    position: absolute;
    width: 12px;
    background: var(--accent);
  }
  .edge-tab--left { left: 0; top: 360px; height: 120px; border-radius: 0 6px 6px 0; }
  .edge-tab--right { right: 0; top: 150px; height: 130px; border-radius: 6px 0 0 6px; }

  .brand {
    position: absolute;
    left: 250px; top: 110px;
    display: flex; align-items: center; gap: 18px;
  }
  .brand-square {
    width: 44px; height: 44px;
    background: var(--accent);
  }
  .brand-name {
    font-family: "Questrial", sans-serif;
    font-size: 50px;
    color: var(--ink-grey);
    letter-spacing: 1px;
    line-height: 1;
  }

  .person {
    position: absolute;
    right: 480px; top: 380px;
    text-align: right;
  }
  .person-name {
    font-family: "Arimo", sans-serif;
    font-weight: 700;
    font-size: 25px;
    color: var(--accent);
  }
  .person-role {
    font-family: "Arimo", sans-serif;
    font-weight: 700;
    font-size: 16px;
    color: var(--ink-grey);
    margin-top: 6px;
  }

  .divider {
    position: absolute;
    left: 440px; top: 330px;
    width: 1px; height: 140px;
    background: var(--divider);
  }

  .contact-list {
    position: absolute;
    left: 462px; top: 330px;
    list-style: none;
  }
  .contact-item {
    display: flex; align-items: center; gap: 14px;
    height: 30px;
    margin-bottom: 10px;
    font-family: "Tinos", serif;
    font-size: 20px;
    color: var(--text-dark);
  }
  .contact-icon { width: 20px; height: 20px; flex: none; }
</style>
</head>
<body>
  <main class="business-card">
    <span class="edge-tab edge-tab--left"></span>
    <span class="edge-tab edge-tab--right"></span>

    <div class="brand">
      <span class="brand-square"></span>
      <span class="brand-name">Harbourlight ceramics Ltd</span>
    </div>

    <div class="person">
      <p class="person-name">Colin Ashby-Rhodes</p>
      <p class="person-role">Director</p>
    </div>

    <span class="divider"></span>

    <ul class="contact-list">
      <li class="contact-item">
        <svg class="contact-icon" viewBox="0 0 20 20" aria-hidden="true">
          <rect x="5" y="1" width="10" height="18" rx="2" fill="none" stroke="var(--accent)" stroke-width="2"/>
          <rect x="7" y="4" width="6" height="8" fill="var(--accent)"/>
          <circle cx="10" cy="15.5" r="1.3" fill="var(--accent)"/>
        </svg>
        <span>+44 7700 900 418</span>
      </li>
      <li class="contact-item">
        <svg class="contact-icon" viewBox="0 0 20 20" aria-hidden="true">
          <circle cx="10" cy="10" r="3.5" fill="none" stroke="var(--accent)" stroke-width="2"/>
          <path d="M13.5 7v4.5a2 2 0 0 0 4 0V10a7.5 7.5 0 1 0-3 6" fill="none" stroke="var(--accent)" stroke-width="2" stroke-linecap="round"/>
        </svg>
        <span>colin@harbourlightceramics.example</span>
      </li>
      <li class="contact-item">
        <svg class="contact-icon" viewBox="0 0 20 20" aria-hidden="true">
          <circle cx="10" cy="10" r="8" fill="none" stroke="var(--accent)" stroke-width="2"/>
          <ellipse cx="10" cy="10" rx="3.5" ry="8" fill="none" stroke="var(--accent)" stroke-width="1.5"/>
          <line x1="2" y1="10" x2="18" y2="10" stroke="var(--accent)" stroke-width="1.5"/>
        </svg>
        <span>www.harbourlightceramics.example</span>
      </li>
    </ul>
  </main>
</body>
</html>
```